MARLOWE BRIGHT WORKS WEBSITE HOME PAGE AND CHECKOUT PAGES

UPDATE TO BRIEF:

Marlowe Bright Works is a company that provides Charities with the Free Vacation Vouchers that they can use to incentivize people to donate which in turn increases donations for the chairty.

So I need to keep it a little more template like the example url I gave. http://pagefernly.com/marlowe-bright-work/ Because, I am going to provide template to ANY CHARITY TYPE and they just fill in the content into the template and change images or whatever for their charity. So I am really looking for a website template that can be used for multiple and different kinds of charities.

So where the logo would go please use YOUR LOGO HERE generic logo for now

and where ever you promote the Free Vacation Certificate To Las Vegas please add "Brought To You By" (logo marlowe bright works or something...basically its a partnership with the Charity and Marlowe Bright Work)

So Marlowe Bright Work is a marketing company and not a Charity but more of a plug and play platform that allows a charity to accepts donations and immediately deliver the promised incentive offer after donation is made on the website.

When a Charity is able to offer a high perceived value gift for a donation they increase donations.

Target Market(s)

PEOPLE THAT DONATE TO CHARITIES

Industry/Entity Type

Charity

Number of Pages Required

3 page

Requirements
Must have
• One thing i need to add to the website is an Incentive Gift for the Donation.

So I need this tagline and images to make the promotion seem great:
"Donate $100 and Receive A Free 3 Night Vacation Certificate To Las Vegas!"

Maybe show image of vegas or some kind of nice graphic that promotes the vegas vacation as a gift for the $100 donation very well"

I need the payment pages as well. So when someone click Donate Now, the next page is there where they can see their gift that is included with the donation, and also the donation amount...
Nice to have

Should not have

```html
<!DOCTYPE html>
<html lang="en">
<head>
<meta charset="utf-8">
<title>Checkout – Marlowe Bright Works</title>
<link rel="stylesheet" href="https://fonts.googleapis.com/css2?family=Roboto:wght@300;400;500;700&family=Rubik:wght@400;500;600&display=swap">
<style>
:root{
  --cyan:#25bfe6;
  --ink:#2b2f36;
  --muted:#8a8f96;
  --line:#9aa0a6;
  --soft:#dcdfe3;
  --page:#f4f4f4;
  --white:#ffffff;
  --orange:#f47b20;
  --footer:#1a1e26;
}
*{box-sizing:border-box;margin:0;padding:0}
html,body{width:1200px;height:808px;overflow:hidden}
body{position:relative;background:var(--page);font-family:"Roboto",sans-serif;color:var(--ink)}
.abs{position:absolute}

.site-header{position:absolute;left:0;top:0;width:1200px;height:80px;background:var(--white)}
.brand{position:absolute;left:94px;top:30px;display:flex;align-items:center;gap:8px;font-family:"Rubik",sans-serif;font-weight:500;font-size:19px;color:var(--cyan)}
.brand-dot{width:20px;height:20px;border-radius:50%;background:var(--cyan)}
.steps{position:absolute;top:34px;left:696px;height:22px}
.step{position:absolute;top:0;display:flex;align-items:center;gap:6px;font-family:"Rubik",sans-serif;font-weight:500;font-size:12.5px;white-space:nowrap}
.step-num{width:20px;height:20px;border-radius:50%;border:1.5px solid var(--cyan);color:var(--cyan);display:flex;align-items:center;justify-content:center;font-size:11px;font-weight:400}
.step.done .step-num{background:var(--cyan)}
.step.todo{color:#b6bbc0}
.step.todo .step-num{border-color:#c4c8cc;color:#b6bbc0}
.step-line{position:absolute;top:10px;height:1px}

.label{position:absolute;font-size:12px;font-weight:500;color:var(--ink)}
.field{position:absolute;border:1px solid var(--line);background:var(--page);font-size:12px;font-weight:300;color:var(--muted);display:flex;align-items:center;padding:0 9px;justify-content:space-between}
.chev{width:10px;height:6px}
.section-title{position:absolute;left:94px;top:376px;font-family:"Rubik",sans-serif;font-size:13.5px;font-weight:500;color:var(--ink)}
.card-names{display:flex;gap:3px}
.card-name{font-size:7.5px;font-weight:500;color:var(--ink);border:1px solid var(--soft);background:var(--white);padding:3px 3px}
.radio{width:8px;height:8px;border-radius:50%;border:1px solid var(--line);display:inline-block;margin-right:6px}
.radio.on{background:var(--cyan);border-color:var(--cyan);box-shadow:inset 0 0 0 1.5px var(--white)}
.terms{position:absolute;left:101px;top:634px;font-size:10.5px;color:var(--ink)}
.terms u{text-decoration:underline}
.place-order{position:absolute;left:93px;top:654px;width:286px;height:35px;background:var(--cyan);color:var(--white);font-size:12px;display:flex;align-items:center;justify-content:center;box-shadow:0 2px 3px rgba(0,0,0,.12)}

.cart{position:absolute;left:755px;top:123px;width:328px;height:372px;border:1px solid var(--line);background:var(--white)}
.cart-title{position:absolute;left:22px;top:17px;display:flex;align-items:center;gap:11px;font-size:12px;font-weight:500}
.cart-title small{color:var(--cyan);font-size:9px;font-weight:400}
.item{position:absolute;left:24px;width:280px;font-size:9px}
.item b{display:block;font-weight:500;color:var(--ink)}
.item span{color:var(--muted);font-weight:300}
.item .price{position:absolute;right:0;top:0;font-weight:500;color:var(--ink);font-style:normal}
.divider{position:absolute;left:24px;width:283px;height:1px;background:var(--soft)}
.subtotal{position:absolute;right:18px;top:316px;font-size:10px;font-weight:700;color:var(--ink)}
.subtotal em{font-style:normal;font-weight:500;color:var(--muted)}

.promo{position:absolute;left:755px;top:505px;width:328px;height:196px;background:radial-gradient(ellipse at 50% 35%,#3a2f22 0%,#1d1812 55%,#0e0c0a 100%);overflow:hidden}
.promo-glow{position:absolute;left:0;bottom:0;width:100%;height:70px;background:linear-gradient(to top,rgba(196,138,52,.45),rgba(0,0,0,0))}
.promo-copy{position:absolute;left:0;top:42px;width:100%;text-align:center;font-family:"Rubik",sans-serif;font-weight:500;color:var(--white)}
.promo-copy .big{font-size:23px;line-height:28px}
.promo-copy .mid{font-size:17.5px;line-height:23px}
.accent-o{color:var(--orange)}
.accent-c{color:var(--cyan)}
.donate-btn{position:absolute;left:102px;top:125px;width:115px;height:32px;background:var(--orange);color:var(--white);font-family:"Rubik",sans-serif;font-size:10.5px;font-weight:500;display:flex;align-items:center;justify-content:center;box-shadow:2px 2px 0 var(--white)}

.site-footer{position:absolute;left:0;top:747px;width:1200px;height:61px;background:var(--footer);border-top:2px solid var(--cyan);display:flex;align-items:center;justify-content:center;font-size:13px;font-weight:300;color:#8b9098}
.site-footer a{color:var(--cyan);text-decoration:none}
</style>
</head>
<body>

<header class="site-header">
  <div class="brand"><span class="brand-dot"></span>Marlowe Bright Works</div>
  <div class="steps">
    <div class="step done" style="left:0"><span class="step-num">
      <svg width="11" height="10" viewBox="0 0 11 10"><path d="M0.5 1h2l1.4 5.5h5.2l1.2-4H3" fill="none" stroke="#fff" stroke-width="1.2"/><circle cx="4.5" cy="8.5" r="0.9" fill="#fff"/><circle cx="8.3" cy="8.5" r="0.9" fill="#fff"/></svg>
    </span>Shopping Cart</div>
    <div class="step-line" style="left:123px;width:58px;background:var(--cyan)"></div>
    <div class="step" style="left:189px"><span class="step-num">2</span>Checkout</div>
    <div class="step-line" style="left:287px;width:58px;background:#c4c8cc"></div>
    <div class="step todo" style="left:352px"><span class="step-num">3</span>Finish</div>
  </div>
</header>

<main>
  <div class="label" style="left:93px;top:103px">First &amp; Last Name</div>
  <div class="field" style="left:92px;top:123px;width:288px;height:36px">Enter your name</div>

  <div class="label" style="left:93px;top:168px">Email address</div>
  <div class="field" style="left:92px;top:186px;width:288px;height:36px">Enter your valid email id</div>

  <div class="label" style="left:93px;top:232px">Country</div>
  <div class="field" style="left:92px;top:249px;width:288px;height:36px">Select your country
    <svg class="chev" viewBox="0 0 10 6"><path d="M1 1l4 4 4-4" fill="none" stroke="#444" stroke-width="1.2"/></svg></div>

  <div class="label" style="left:93px;top:294px">State/ Country</div>
  <div class="label" style="left:272px;top:294px">Zip/ Post Code</div>
  <div class="field" style="left:92px;top:312px;width:168px;height:36px"></div>
  <div class="field" style="left:271px;top:312px;width:109px;height:36px"></div>

  <div class="section-title">Payment method</div>
  <div class="field" style="left:92px;top:400px;width:288px;height:36px;color:var(--ink);font-weight:400">
    <span><i class="radio on"></i>Credit card</span>
    <span class="card-names"><span class="card-name">Veltra</span><span class="card-name">Amerix</span><span class="card-name">Discora</span><span class="card-name">Mastrel</span></span>
  </div>

  <div class="label" style="left:94px;top:448px">Card number</div>
  <div class="field" style="left:92px;top:467px;width:288px;height:36px">4213 5548 159 9918<span class="card-name">Veltra</span></div>

  <div class="label" style="left:94px;top:513px">Expireation date</div>
  <div class="label" style="left:283px;top:513px">Security code</div>
  <div class="field" style="left:92px;top:530px;width:84px;height:36px">Month
    <svg class="chev" viewBox="0 0 10 6"><path d="M1 1l4 4 4-4" fill="none" stroke="#444" stroke-width="1.2"/></svg></div>
  <div class="field" style="left:183px;top:530px;width:84px;height:36px">Year
    <svg class="chev" viewBox="0 0 10 6"><path d="M1 1l4 4 4-4" fill="none" stroke="#444" stroke-width="1.2"/></svg></div>
  <div class="field" style="left:280px;top:530px;width:99px;height:36px">Three Digit
    <svg width="15" height="15" viewBox="0 0 15 15"><circle cx="7.5" cy="7.5" r="6.5" fill="none" stroke="#666"/><path d="M5.6 5.8a2 2 0 1 1 2.6 1.9c-.5.2-.7.5-.7 1v.6" fill="none" stroke="#666" stroke-width="1"/><circle cx="7.5" cy="11" r=".7" fill="#666"/></svg></div>

  <div class="field" style="left:92px;top:583px;width:288px;height:36px">
    <span><i class="radio"></i>PayQuill</span>
    <span style="font-size:11px;font-weight:500;color:var(--ink)">PayQuill</span>
  </div>

  <p class="terms">By checking the button, to the <u>Term and Condition</u></p>
  <div class="place-order">Place order</div>

  <aside class="cart">
    <div class="cart-title">
      <svg width="18" height="17" viewBox="0 0 18 17"><path d="M1 1.5h2.8l2 9h8.6l1.8-6.5H5" fill="none" stroke="#333" stroke-width="1.2"/><circle cx="7" cy="14.3" r="1.3" fill="none" stroke="#333"/><circle cx="13.5" cy="14.3" r="1.3" fill="none" stroke="#333"/></svg>
      <span>Cart summary <small>(236)</small></span>
    </div>
    <div class="item" style="top:63px"><b>Lorem ipsum dolor sit amet,</b><span>consectetur adipiscing elit</span><i class="price">$ 49.00</i></div>
    <div class="divider" style="top:100px"></div>
    <div class="item" style="top:119px"><b>Lorem ipsum dolor sit amet,</b><span>consectetur adipiscing elit</span><i class="price">$ 49.00</i></div>
    <div class="divider" style="top:164px"></div>
    <div class="item" style="top:175px"><b>Lorem ipsum dolor sit amet,</b><span>consectetur adipiscing elit</span><i class="price">$ 49.00</i></div>
    <div class="divider" style="top:228px"></div>
    <div class="item" style="top:246px"><b>Lorem ipsum dolor sit amet,</b><span>consectetur adipiscing elit</span><i class="price">$ 49.00</i></div>
    <div class="subtotal"><em>Sub total:</em> $ 1024.44</div>
  </aside>

  <section class="promo">
    <div class="abs" role="img" aria-label="Night skyline of the Las Vegas strip with lit hotels" style="inset:0">
      <div class="promo-glow"></div>
    </div>
    <div class="promo-copy">
      <div class="big">Donate <span class="accent-o">$100</span></div>
      <div class="mid">Get A Free <span class="accent-c">3 Night</span> Vacation</div>
      <div class="mid">Certificate For <span class="accent-c">Las Vega</span></div>
    </div>
    <div class="donate-btn">DONATE NOW</div>
  </section>
</main>

<footer class="site-footer">© 2020&nbsp;<a href="#">Marlowe Bright Work</a>. All Right Reserved.</footer>

</body>
</html>
```